Kalvoria - a property developer - Website design

Hi all!
Exciting new project for you! :)
We are looking for some creative/modern designs to best represent us as a company.
Please have a look at the following link: huhu.kalvoria.example to get an idea about who we are and what we do.
The 'Main Page' of the HP should be neatly arranged, easy to navigate, contain several pictures (changing every 10 seconds or so) that should reflect that we are property developers.
The navigation points ('About us', 'Projects' 'Investment', 'Contact Us', 'Legal Notice') should be included in the Design (again under every navigation point, pictures may be added - that reflect our profession and/or the subsection)
What we will need at the end of the day is a fully functional site - i.e: a site that is designed and programmed with backend/wordpress, to allow us to make changes anytime we feel like it.
Further questions?! Don't hesitate to contact me! Thanks :)
Target Market(s)
Real Estate Development/Building sector
Industry/Entity Type
Real Estate Development
Number of Pages Required
5+ page
Look and feel

```html
<!DOCTYPE html>
<html lang="en">
<head>
<meta charset="utf-8">
<title>Kalvoria – Property Developer</title>
<link href="https://fonts.googleapis.com/css2?family=Roboto:wght@400;500&family=Lato:ital,wght@0,400;0,700;1,400&family=Pathway+Gothic+One&display=swap" rel="stylesheet">
<style>
:root{
  --yellow:#f7dc00;
  --black:#050505;
  --ink:#222;
  --text:#4a4a4a;
  --grey-band:#6b6b6b;
  --card-head:#6e6d69;
  --section-bg:#f4f4f4;
  --footer:#2b2b2b;
  --footer-deep:#1f1f1f;
  --footer-text:#e6e6e6;
  --rule:#bdbdbd;
}
*{box-sizing:border-box;margin:0;padding:0}
html,body{width:1005px;height:1200px;overflow:hidden;background:#fff}
body{position:relative;font-family:'Lato',sans-serif;color:var(--text)}
.abs{position:absolute}

/* header */
.brand{left:110px;top:18px;display:flex;align-items:center;gap:8px}
.brand-mark{width:26px;height:52px;background:var(--black);border:3px solid var(--black)}
.brand-name{font-family:'Roboto',sans-serif;font-weight:400;font-size:40px;letter-spacing:3px;color:var(--black);line-height:40px}
.brand-sub{font-family:'Roboto',sans-serif;font-size:10px;color:var(--black);letter-spacing:1px;margin-top:2px}
.social{display:flex;gap:9px}
.social span{width:14px;height:14px;border-radius:50%;background:#6b6b6b;display:block}
.top-social{left:813px;top:26px}
.call{left:702px;top:55px;font-family:'Roboto',sans-serif;font-size:19px;color:#666;display:flex;align-items:center;gap:6px}

/* nav */
.nav{left:0;top:95px;width:1005px;height:39px;background:var(--black)}
.nav ul{list-style:none;display:flex;margin-left:110px;height:39px}
.nav li{font-family:'Roboto',sans-serif;font-size:15px;color:#fff;height:39px;line-height:39px;padding:0 34px;border-right:1px solid #333}
.nav li.active{background:var(--yellow);color:var(--black);padding:0 25px;border:none}
.nav li:last-child{border:none}

/* hero */
.hero{left:0;top:134px;width:1005px;height:277px;background:linear-gradient(180deg,#9fb2bf 0%,#b8a88f 40%,#7e7466 75%,#5f5a52 100%)}
.hero-band{left:0;top:411px;width:1005px;height:52px;background:var(--grey-band)}
.hero-caption{left:133px;top:418px;font-family:'Pathway Gothic One',sans-serif;font-size:30px;color:#fff;letter-spacing:.3px}
.dots{left:828px;top:431px;display:flex;gap:4px}
.dots span{width:12px;height:12px;border-radius:50%;background:#fff}
.dots span:first-child{background:var(--yellow)}

/* cards */
.card{top:496px;width:246px;height:228px;background:#fafafa;border:1px solid #d8d8d8;border-radius:6px;box-shadow:0 14px 10px -10px rgba(0,0,0,.25)}
.card-tab{position:absolute;left:16px;top:-7px;width:214px;height:31px;background:var(--card-head);clip-path:polygon(0 0,100% 0,92% 100%,8% 100%);border-radius:6px 6px 0 0;color:#fff;font-family:'Roboto',sans-serif;font-size:18px;text-align:center;line-height:32px}
.card-photo{position:absolute;left:11px;top:36px;width:224px;height:108px}
.card p{position:absolute;left:10px;top:153px;width:228px;font-size:11.4px;line-height:15px;color:#555}
.card a{position:absolute;right:13px;top:206px;font-size:9.5px;font-weight:700;color:#666;text-decoration:none}

/* middle section */
.middle{left:0;top:760px;width:1005px;height:162px;background:var(--section-bg);border-top:1px solid #e3e3e3;border-bottom:1px solid #e3e3e3}
.h-section{font-family:'Roboto',sans-serif;font-size:18px;color:var(--ink)}
.testi-title{left:117px;top:774px}
.testi-arrows{left:594px;top:782px;font-size:14px;color:#555;letter-spacing:6px}
.testi-rule{left:117px;top:805px;width:506px;border-top:1px dotted #aaa}
.avatar{left:119px;top:816px;width:89px;height:89px;border-radius:50%;border:4px solid #fff;box-shadow:0 0 0 1px #ccc;background:radial-gradient(circle,#e6c79e 0%,#c9a574 60%,#9c8a74 100%)}
.quote-box{left:232px;top:814px;width:392px;height:91px;background:#fff;border:1px solid #ddd;border-radius:4px}
.quote-box p{position:absolute;left:13px;top:8px;width:370px;font-style:italic;font-size:10.8px;line-height:17.5px;color:#666}
.quote-box .who{position:absolute;left:14px;top:66px;font-size:13px;color:#333}
.resources{left:642px;top:777px;width:246px;height:128px;background:#fff;border:1px solid #ddd;border-radius:3px}
.resources h3{position:absolute;left:12px;top:6px;font-weight:400}
.resources .rule{position:absolute;left:8px;top:29px;width:228px;border-top:1px dotted #aaa}
.resources p{position:absolute;left:8px;top:37px;width:150px;font-size:11px;line-height:17px;color:#444}
.btn-dark{position:absolute;left:8px;top:83px;background:#555;color:#fff;font-family:'Roboto',sans-serif;font-size:12px;padding:6px 9px;border-radius:2px}
.res-photo{position:absolute;left:128px;top:40px;width:116px;height:86px;background:radial-gradient(ellipse at 70% 75%,#c89a5a 0%,#d9b483 35%,rgba(255,255,255,0) 70%),radial-gradient(ellipse at 75% 25%,#7fb33a 0%,rgba(255,255,255,0) 45%)}

/* footer */
.footer{left:0;top:953px;width:1005px;height:215px;background:var(--footer);border-top:4px solid var(--yellow)}
.f-col{top:977px;color:var(--footer-text)}
.f-col h4{font-family:'Lato',sans-serif;font-weight:700;font-size:15px;color:#f2f2f2;padding-bottom:9px;border-bottom:1px dotted #666}
.f-sep{top:977px;width:1px;height:155px;background:#383838}
.links{list-style:none;font-size:11.5px}
.links li{height:23.5px;padding-left:14px;position:relative}
.links li::before{content:'›';position:absolute;left:2px;top:-2px;color:#aaa}
.f-text{font-size:11.5px;line-height:17px}
.field{width:178px;height:26px;background:#fff;border-radius:2px;font-size:10px;font-style:italic;color:#555;padding:7px 9px}
.btn-sub{display:inline-block;background:#5a5a5a;color:#fff;font-family:'Roboto',sans-serif;font-weight:500;font-size:11.5px;padding:6px 9px;border-radius:2px}
.contact-row{display:flex;gap:14px;align-items:flex-start;font-size:11.5px;line-height:16px}
.contact-row svg{flex:none;margin-top:1px}
.f-brand{left:714px;top:1044px;display:flex;align-items:center;gap:7px}
.f-brand .brand-mark{width:18px;height:35px;background:none;border:2px solid #bbb}
.f-brand .brand-name{color:#c8c8c8;font-size:26px;line-height:26px;letter-spacing:2px}
.f-brand .brand-sub{color:#bbb;font-size:7px}
.bottom{left:0;top:1168px;width:1005px;height:32px;background:var(--footer-deep);font-size:11.5px;color:#ddd}
.copy{position:absolute;left:117px;top:9px}
.copy a{color:var(--yellow);margin-left:8px;font-size:13px}
.follow{position:absolute;left:774px;top:8px;display:flex;gap:8px;align-items:center;font-weight:700;font-size:12px}
.follow .social span{background:#ddd;width:11px;height:11px}
</style>
</head>
<body>

<header>
  <div class="abs brand">
    <div class="brand-mark"></div>
    <div>
      <div class="brand-name">KALVORIA</div>
      <div class="brand-sub">KALVORIA.EXAMPLE</div>
    </div>
  </div>
  <div class="abs social top-social"><span></span><span></span><span></span></div>
  <div class="abs call">
    <svg width="14" height="18" viewBox="0 0 14 18"><path d="M3 1l3 3-2 2c1 3 3 6 5 7l2-2 3 3-2 3C6 17 1 10 1 3z" fill="#666"/></svg>
    Call: +43 1 555 0140
  </div>
</header>

<nav class="abs nav">
  <ul>
    <li class="active">HOME</li>
    <li>ABOUT US</li>
    <li>PROJECTS</li>
    <li>INVESTMENT</li>
    <li>CONTACT US</li>
  </ul>
</nav>

<section>
  <div class="abs hero" role="img" aria-label="Aerial photo of a dense city centre with high-rise towers and a harbour"></div>
  <div class="abs hero-band"></div>
  <div class="abs hero-caption">Quality, Skill And Experience : Everything Under One Roof</div>
  <div class="abs dots"><span></span><span></span><span></span><span></span></div>
</section>

<section>
  <article class="abs card" style="left:118px">
    <div class="card-tab">ABOUT US</div>
    <div class="card-photo" role="img" aria-label="Photo of a handshake in front of a building site with a hard hat" style="background:linear-gradient(120deg,#8fb5d8 0%,#c9cfd4 45%,#e6c9a8 70%,#d9c23a 100%)"></div>
    <p>Lorem ipsum dolor sit amet, consec adipiscing elit, sed diam nonummy nibh euismo tincidunt ut laoreet dolore magna.</p>
    <a href="#">Read more »</a>
  </article>
  <article class="abs card" style="left:379px">
    <div class="card-tab">OUR PROJECTS</div>
    <div class="card-photo" role="img" aria-label="Photo of a tower under construction with cranes against a blue sky" style="background:linear-gradient(180deg,#3f7fc6 0%,#7aa8d8 50%,#8a8478 80%,#5c5850 100%)"></div>
    <p>Lorem ipsum dolor sit amet, consec adipiscing elit, sed diam nonummy nibh euismo tincidunt ut laoreet dolore magna.</p>
    <a href="#">Read more »</a>
  </article>
  <article class="abs card" style="left:641px">
    <div class="card-tab">INVESTMENTS</div>
    <div class="card-photo" role="img" aria-label="Illustration of a compass pointing towards the word investment" style="background:radial-gradient(circle at 45% 65%,#4f86c4 0%,#1f4f8c 55%,#0f2f5c 100%)"></div>
    <p>Lorem ipsum dolor sit amet, consec adipiscing elit, sed diam nonummy nibh euismo tincidunt ut laoreet dolore magna.</p>
    <a href="#">Read more »</a>
  </article>
</section>

<section>
  <div class="abs middle"></div>
  <h3 class="abs h-section testi-title" style="font-weight:400">CLIENT TESTIMONIALS</h3>
  <div class="abs testi-arrows">‹ ›</div>
  <div class="abs testi-rule"></div>
  <div class="abs avatar" role="img" aria-label="Portrait photo of the client"></div>
  <div class="abs quote-box">
    <p>“ Lorem ipsum dolor sit amet, consecte ipsumi adipiscing elit, nonummy nibh euismod tinci laoreet dolore magna aliquam erat volutpat. U wis enim ad minim veniam, quis nostrud exerc ullamcorper suscipit. ”</p>
    <div class="who">Mara Lindqvist</div>
  </div>
  <div class="abs resources">
    <h3 class="h-section">RESOURCES</h3>
    <div class="rule"></div>
    <p>Lorem ipsum dolor sit amet, consectetu adipiscing elit</p>
    <div class="res-photo" role="img" aria-label="Photo of a young plant growing from a pile of coins"></div>
    <div class="btn-dark">KNOW MORE</div>
  </div>
</section>

<footer>
  <div class="abs footer"></div>
  <div class="abs f-col" style="left:118px;width:131px">
    <h4>Quick Links</h4>
    <ul class="links" style="margin-top:9px">
      <li>Home</li><li>Projects</li><li>Investment</li><li>Resources</li><li>Contact Us</li>
    </ul>
  </div>
  <div class="abs f-sep" style="left:270px"></div>
  <div class="abs f-col" style="left:293px;width:181px">
    <h4>Newsletter Signup</h4>
    <p class="f-text" style="margin:10px 0 9px 2px">Lorem ipsum dolor sit amet,consecte euismod tincidunt.</p>
    <div class="field">Email Address</div>
    <div class="btn-sub" style="margin-top:12px">SUBSCRIBE</div>
  </div>
  <div class="abs f-sep" style="left:496px"></div>
  <div class="abs f-col" style="left:519px;width:153px">
    <h4>Contact Detail</h4>
    <div class="contact-row" style="margin-top:12px">
      <svg width="12" height="16" viewBox="0 0 12 16"><path d="M6 0a6 6 0 0 0-6 6c0 4 6 10 6 10s6-6 6-10a6 6 0 0 0-6-6zm0 8.5A2.5 2.5 0 1 1 6 3.5a2.5 2.5 0 0 1 0 5z" fill="#eee"/></svg>
      <span>Lindenweg 7/TOP 4B<br>1220 Vienna - Austria</span>
    </div>
    <div class="contact-row" style="margin-top:9px;font-weight:700">
      <svg width="12" height="14" viewBox="0 0 14 18"><path d="M3 1l3 3-2 2c1 3 3 6 5 7l2-2 3 3-2 3C6 17 1 10 1 3z" fill="#eee"/></svg>
      <span>+43 1 555 0140</span>
    </div>
    <div class="contact-row" style="margin-top:10px;font-weight:700">
      <svg width="13" height="13" viewBox="0 0 13 13"><rect x="3" y="0" width="7" height="4" fill="#eee"/><rect x="0" y="4" width="13" height="6" rx="1" fill="#eee"/><rect x="3" y="8" width="7" height="5" fill="#eee" stroke="#2b2b2b"/></svg>
      <span>+43 1 555 0141</span>
    </div>
    <div class="contact-row" style="margin-top:10px">
      <svg width="12" height="10" viewBox="0 0 12 10"><rect width="12" height="10" fill="#eee"/><path d="M0 0l6 5 6-5" stroke="#2b2b2b" fill="none"/></svg>
      <span>info@kalvoria.example</span>
    </div>
  </div>
  <div class="abs f-sep" style="left:692px"></div>
  <div class="abs f-brand">
    <div class="brand-mark"></div>
    <div>
      <div class="brand-name">KALVORIA</div>
      <div class="brand-sub">KALVORIA.EXAMPLE</div>
    </div>
  </div>
  <div class="abs bottom">
    <div class="copy">Copyright © 2015 KALVORIA | All Rights Reserved. <a href="#">Legal Notice</a></div>
    <div class="follow">Follow Us: <div class="social"><span></span><span></span><span></span></div></div>
  </div>
</footer>

</body>
</html>
```